Election features for a political website

The Hearthside Ledger (www.hearthsideledger.example)
Web banner designs
Please have a look at The Hearthside Ledger website (www.hearthsideledger.example). We are seeking to add an advertising style banner at the top of every page and post. It will run right across the page (1024 pixels) and be in the region of 200 pixels vertically. (Please advise on what looks best size wise.
The banner will be a slider, operated in a similar way to the current homepage slider. There will be four items on the slider, and so we need four designs that match the aesthetic feel of the website. Each slider will link through to posts on the website.
1.
Headline: OUR CANDIDATE OF THE DAY
Space for a name, head and shoulders picture of the person to be dropped in and a one line reason. This will need to be in an editable format as this image will be changed each day for one month.
2.
Headline: HERO OF THE DAY
Space for name and a one line reason. This will need to be in an editable format as this image will be changed each day for one month.
3.
Headline: VILLAIN OF THE DAY
Space for name of the person to be dropped in and a one line reason. This will need to be in an editable format as this image will be changed each day for one month.
4.
Headline: THL Poll – [Date]
If the election was today, who would you vote for?
Clickable options:
Brightfolders
Ashvel
Marden Alliancers
Vornu
Tally
Other
Can a poll widget be added to the banner? We would like this poll to reset each day and then pool the results into a graph day by day over a one month period.
Reason: Payment is now guaranteed. We would like to see more options.

```html
<!DOCTYPE html>
<html lang="en">
<head>
<meta charset="utf-8">
<title>THL Poll Banner</title>
<link href="https://fonts.googleapis.com/css2?family=Arimo:wght@700&family=Gelasio:wght@700&family=Tinos&display=swap" rel="stylesheet">
<style>
  :root {
    --navy: #00548a;
    --header-blue: #1f6594;
    --stripe-blue: #0a86d2;
    --white: #ffffff;
    --note-blue: #1f5a8a;
    --page: #ffffff;
  }
  * { margin: 0; padding: 0; box-sizing: border-box; }
  html, body {
    width: 1200px;
    height: 420px;
    overflow: hidden;
    background: var(--page);
  }
  .canvas {
    position: relative;
    width: 1200px;
    height: 420px;
  }
  .poll-banner {
    position: absolute;
    left: 12px;
    top: 10px;
    width: 1024px;
    height: 400px;
    background: var(--navy);
    color: var(--white);
    font-family: "Gelasio", Georgia, serif;
  }
  .poll-header {
    position: absolute;
    left: 0;
    top: 34px;
    width: 100%;
    height: 100px;
    background: var(--header-blue);
    border-top: 6px solid var(--stripe-blue);
    border-bottom: 6px solid var(--stripe-blue);
  }
  .poll-title {
    position: absolute;
    left: 39px;
    top: 16px;
    font-size: 45px;
    font-weight: 700;
    line-height: 1.2;
  }
  .poll-date {
    position: absolute;
    right: 38px;
    top: 22px;
    font-family: "Arimo", Arial, sans-serif;
    font-size: 37px;
    font-weight: 700;
    line-height: 1.2;
  }
  .poll-question {
    position: absolute;
    left: 42px;
    top: 168px;
    font-size: 22px;
    font-weight: 700;
    line-height: 1.2;
  }
  .poll-options {
    list-style: none;
  }
  .poll-option {
    position: absolute;
    display: flex;
    align-items: center;
    font-size: 24px;
    font-weight: 700;
    line-height: 1;
  }
  .radio {
    width: 29px;
    height: 29px;
    border-radius: 50%;
    background: var(--white);
    margin-right: 28px;
    flex-shrink: 0;
  }
  .radio--selected {
    background: var(--navy);
    border: 4px solid var(--white);
  }
  .col-1 { left: 38px; }
  .col-2 { left: 409px; }
  .col-2 .radio { margin-right: 26px; }
  .row-1 { top: 231px; }
  .row-2 { top: 284px; }
  .row-3 { top: 335px; }
  .submit-button {
    position: absolute;
    left: 835px;
    top: 317px;
    width: 151px;
    height: 51px;
    background: var(--white);
    color: var(--navy);
    border-radius: 4px;
    font-family: "Arimo", Arial, sans-serif;
    font-size: 25px;
    font-weight: 700;
    display: flex;
    align-items: center;
    justify-content: center;
  }
  .size-note {
    position: absolute;
    left: 1082px;
    top: 175px;
    font-family: "Tinos", "Times New Roman", serif;
    font-size: 17px;
    line-height: 30px;
    color: var(--note-blue);
  }
</style>
</head>
<body>
<div class="canvas">
  <section class="poll-banner" aria-label="THL Poll">
    <header class="poll-header">
      <h1 class="poll-title">THL Poll</h1>
      <div class="poll-date">02-09-2015</div>
    </header>
    <p class="poll-question">If the election was today, who would you vote for?</p>
    <ul class="poll-options">
      <li class="poll-option col-1 row-1"><span class="radio"></span>Brightfolders</li>
      <li class="poll-option col-1 row-2"><span class="radio radio--selected"></span>Ashvel</li>
      <li class="poll-option col-1 row-3"><span class="radio"></span>Marden Alliancers</li>
      <li class="poll-option col-2 row-1"><span class="radio"></span>Vornu</li>
      <li class="poll-option col-2 row-2"><span class="radio"></span>Tally</li>
      <li class="poll-option col-2 row-3"><span class="radio"></span>Other</li>
    </ul>
    <div class="submit-button">SUBMIT</div>
  </section>
  <div class="size-note">BANNER<br>SIZE<br>1024x400</div>
</div>
</body>
</html>
```